Sales and Lettings Boards

Hello, please see attached our sales and lettings boards for our estate agency. These were "designed" by the sign writers. As you can see they are pretty flat and boring - could you work your magic and make them stand out please? I've also attached the logo files. Many thanks, Glen

Target Market(s)

Consumers - residential sale property sales and lettings

Industry/Entity Type

Real Estate Agent

```html
<!DOCTYPE html>
<html lang="en">
<head>
<meta charset="utf-8">
<title>Kestrel Property – For Sale Board</title>
<link rel="stylesheet" href="https://fonts.googleapis.com/css2?family=Montserrat:wght@600;700&display=swap">
<style>
  :root {
    --charcoal: #4a4b4d;
    --green: #62bb46;
    --green-deep: #3d8a2b;
    --board-top: #ffffff;
    --board-fade: #c9c9c9;
    --white: #ffffff;
  }
  html, body {
    margin: 0;
    padding: 0;
    width: 1200px;
    height: 1000px;
    overflow: hidden;
    background: var(--board-top);
  }
  .sale-board {
    position: relative;
    width: 1200px;
    height: 1000px;
    overflow: hidden;
    font-family: "Montserrat", Arial, sans-serif;
  }
  .board-shapes {
    position: absolute;
    inset: 0;
  }
  .brand-name,
  .brand-line,
  .board-headline,
  .contact-phone,
  .contact-web {
    position: absolute;
    left: 0;
    width: 1200px;
    margin: 0;
    text-align: center;
    line-height: 1;
  }
  .brand-name {
    top: 28px;
    font-size: 180px;
    font-weight: 700;
    letter-spacing: -2px;
    color: var(--charcoal);
  }
  .brand-line {
    top: 270px;
    font-size: 88px;
    font-weight: 700;
    color: var(--charcoal);
  }
  .board-headline {
    top: 449px;
    font-size: 160px;
    font-weight: 600;
    color: var(--white);
  }
  .contact-phone {
    top: 783px;
    font-size: 88px;
    font-weight: 700;
    color: var(--white);
    letter-spacing: 1px;
  }
  .contact-web {
    top: 880px;
    font-size: 58px;
    font-weight: 600;
    color: var(--white);
  }
</style>
</head>
<body>
<main class="sale-board">
  <svg class="board-shapes" width="1200" height="1000" viewBox="0 0 1200 1000" aria-hidden="true">
    <defs>
      <linearGradient id="board-fade" x1="0" y1="0" x2="0" y2="1">
        <stop offset="0" stop-color="var(--board-top)"/>
        <stop offset="0.45" stop-color="var(--board-fade)"/>
      </linearGradient>
      <linearGradient id="band-fade" x1="0" y1="0" x2="0" y2="1">
        <stop offset="0.3" stop-color="#3f8c2d"/>
        <stop offset="0.75" stop-color="#62bb46"/>
      </linearGradient>
    </defs>
    <rect class="board-backdrop" width="1200" height="1000" fill="url(#board-fade)"/>
    <path class="band-edge" d="M0 523 Q600 266 1200 484 L1200 1000 L0 1000 Z" fill="var(--green)"/>
    <path class="band-body" d="M0 545 Q600 300 1200 505 L1200 1000 L0 1000 Z" fill="url(#band-fade)"/>
    <path class="band-underline" d="M0 770 Q600 540 1200 760 L1200 1000 L0 1000 Z" fill="var(--green-deep)"/>
    <path class="contact-panel" d="M0 790 Q600 520 1200 790 L1200 1000 L0 1000 Z" fill="var(--charcoal)"/>
    <g class="phone-badge" transform="translate(598 690)">
      <circle r="66" fill="var(--green-deep)" stroke="var(--white)" stroke-width="4"/>
      <path transform="translate(-33 -33) scale(2.75)" fill="var(--white)"
        d="M6.6 10.8c1.4 2.8 3.8 5.1 6.6 6.6l2.2-2.2c.3-.3.7-.4 1-.2 1.1.4 2.3.6 3.6.6.6 0 1 .4 1 1V20c0 .6-.4 1-1 1C10.6 21 3 13.4 3 4c0-.6.4-1 1-1h3.5c.6 0 1 .4 1 1 0 1.3.2 2.5.6 3.6.1.3 0 .7-.2 1L6.6 10.8z"/>
    </g>
  </svg>

  <h1 class="brand-name">KESTREL</h1>
  <p class="brand-line">PROPERTY</p>
  <h2 class="board-headline">FOR SALE</h2>
  <p class="contact-phone">01632 960418</p>
  <p class="contact-web">www.kestrel-estates.co.uk</p>
</main>
</body>
</html>
```